10-year customer thank you card

We want a greeting card that our sales reps can send to companies/customers who have been with our company for 10 or more years. We're a software company, our corporate color is blue but we also like green, orange, and purple. We'd like something rather minimal/simplistic for this card, perhaps building off our tree logo. We're really open to ideas for this one. You must use the template files that are uploaded. Copy included in 10 year thank you card file; the copy may change based on how it looks when laid out
Updates

I updated our brief. We'd prefer a sans serif font. I also uploaded a blank infographic image that includes more of our approved colors.

Industry/Entity Type

Software

Font styles to use
Sans Serif

```html
<!DOCTYPE html>
<html lang="en">
<head>
<meta charset="utf-8">
<title>Ten Years – Thank You Card</title>
<link rel="stylesheet" href="https://fonts.googleapis.com/css2?family=Raleway:wght@400;500&display=swap">
<style>
  :root {
    --card-bg: #ffffff;
    --card-edge: #e4e7eb;
    --brand-blue: #1b7fc3;
    --brand-green: #a9cf46;
    --brand-orange: #f68b35;
    --brand-purple: #5a3f93;
  }
  html, body {
    margin: 0;
    padding: 0;
    width: 1200px;
    height: 841px;
    overflow: hidden;
    background: var(--card-bg);
  }
  .card {
    position: relative;
    width: 1200px;
    height: 841px;
    box-sizing: border-box;
    border: 2px solid var(--card-edge);
    background: var(--card-bg);
  }
  .motif-row {
    position: absolute;
    left: 36px;
    top: 465px;
    width: 1099px;
    height: 113px;
    display: grid;
    grid-template-columns: repeat(10, 84px);
    justify-content: space-between;
  }
  .motif-slot {
    height: 113px;
    border-radius: 42px 42px 6px 6px;
  }
  .motif-slot--blue { background: var(--brand-blue); }
  .motif-slot--green { background: var(--brand-green); }
  .motif-slot--orange { background: var(--brand-orange); }
  .motif-slot--purple { background: var(--brand-purple); }
  .thank-you {
    position: absolute;
    left: 0;
    right: 0;
    top: 636px;
    margin: 0;
    text-align: center;
    font-family: "Raleway", "Helvetica Neue", Arial, sans-serif;
    font-weight: 400;
    font-variant: small-caps;
    font-size: 60px;
    line-height: 1.2;
    letter-spacing: 1px;
    color: var(--brand-blue);
    white-space: pre;
  }
</style>
</head>
<body>
  <main class="card">
    <div class="motif-row" role="img" aria-label="Row of ten stylised trees alternating blue, green, orange and purple">
      <span class="motif-slot motif-slot--blue" aria-hidden="true"></span>
      <span class="motif-slot motif-slot--green" aria-hidden="true"></span>
      <span class="motif-slot motif-slot--orange" aria-hidden="true"></span>
      <span class="motif-slot motif-slot--purple" aria-hidden="true"></span>
      <span class="motif-slot motif-slot--blue" aria-hidden="true"></span>
      <span class="motif-slot motif-slot--green" aria-hidden="true"></span>
      <span class="motif-slot motif-slot--orange" aria-hidden="true"></span>
      <span class="motif-slot motif-slot--purple" aria-hidden="true"></span>
      <span class="motif-slot motif-slot--blue" aria-hidden="true"></span>
      <span class="motif-slot motif-slot--green" aria-hidden="true"></span>
    </div>
    <h1 class="thank-you">Ten Years.  Thank you!</h1>
  </main>
</body>
</html>
```